Wix Landing Page for Cutting-Edge Healthcare Concussion Supplement

Wix Website Design Brief: Velmorastrin+ Landing Page for Market Testing
Description:
Design a modern Wix landing page for Velmorastrin+, an innovative concussion recovery and brain health supplement from a cutting-edge healthcare company. The page will focus on market testing, lead generation, and customer engagement with educational content.
________________________________________
1. Overview of Velmorastrin+
Business Name: Velmorastrin+
Industry: Health & Wellness / Nutraceutical Supplements
Project Goal:
Velmorastrin+ is a premium nutraceutical supplement designed to help prevent concussions and accelerate recovery from traumatic brain injuries (TBI). Every year, millions of people suffer concussions—whether from contact sports, military service, or accidents—which can lead to both short- and long-term cognitive, emotional, and physical impairments. Current treatment options are limited to rest and rehabilitation, with no KTV-approved medications to directly aid recovery.
Velmorastrin+ seeks to fill this gap by providing a science-backed, multi-ingredient formulation designed to reduce neuroinflammation, oxidative stress, and support mitochondrial function, helping the brain recover faster and more effectively. Our goal is to raise awareness of this innovative approach to concussion care, test market interest, and build an early community of customers and healthcare providers. This project will create a Wix-based landing page for market testing, lead generation, and educational outreach to gauge demand and prepare for future product launches.
2. Target Audience
Primary Audience:
1. Athletes:
o Individuals in high-contact sports (e.g., football, rugby, soccer) at risk for concussions, seeking supplements to help protect brain health and accelerate recovery.
2. Military Personnel and Veterans:
o Active-duty service members and veterans who are at higher risk of Traumatic Brain Injuries (TBI) and are interested in maintaining optimal cognitive function and recovery.
3. Older Adults:
o Individuals aged 60+ concerned about cognitive health and recovery after falls or injuries leading to concussions, looking for proactive brain health support.
4. Healthcare Professionals:
o Physicians, therapists, and other healthcare providers seeking cutting-edge, evidence-based supplements to recommend to patients dealing with concussions or TBI.
3. Landing Page Objectives
1. Market Testing:
The page’s primary goal is to gauge potential demand for Velmorastrin+ and collect valuable data through email sign-ups, lead generation forms, and user engagement.
2. Educational Content:
Provide high-level, non-proprietary information about concussions, brain health, and how Velmorastrin+ can support recovery. Emphasize the science-backed nature of the supplement without revealing the full ingredient formula. Position this content strategically to educate visitors before they convert.
3. Lead Capture:
Use compelling calls-to-action (CTAs) to encourage visitors to sign up for a waitlist, download an eBook on concussion recovery, or join an email list for updates. The primary goal is to gather emails and generate leads for future marketing efforts.
4. User Engagement and Blog:
Incorporate a blog section to provide visitors with more in-depth content about concussions, brain health, and recovery strategies. The blog should offer expert articles, recovery tips, and current scientific findings, helping to establish Velmorastrin+ as an authority on the subject. Ensure visitors are engaged with informative content, testimonials, and interactive elements like quizzes or polls that encourage participation and capture interest.
4. Key Design Requirements
4.1 General Style:
• Clean and Modern Design:
The landing page should have a professional, trustworthy feel while being modern and minimalistic. It should align with the health and wellness industry, using visuals and design elements that convey trust, support, and scientific credibility.
• Easy-to-Navigate Layout:
The page must be intuitive, with clearly defined sections that guide users effortlessly through the content, leading them to the CTA forms.
4.2 Specific Sections to Include:
1. Hero Section (Above the Fold):
o Headline: A compelling headline such as “Guard Your Days. Bounce Back with Velmorastrin+.”
o Subtext: Briefly describe the supplement’s primary benefits, e.g., “Advanced nutraceutical formulation supporting brain health and faster concussion recovery.”
o Call to Action (CTA): Prominently feature a button like “Join the Waitlist” or “Download Free Recovery Guide.”
o Include a visually appealing background image or hero image that represents brain health or protection.
2. Benefits Section:
o Highlight key benefits in bullet points, such as:
Faster recovery from concussions – Velmorastrin+ accelerates recovery by reducing neuroinflammation and oxidative stress.
Protection against long-term brain damage – The supplement helps prevent lasting cognitive impairment from multiple or severe concussions.
Scientifically backed multi-pathway neuroprotection – Targets inflammation, oxidative damage, mitochondrial function, and synaptic health.
Improved cognitive function – Enhances mental clarity, focus, and energy post-concussion.
Preventive benefits for high-risk individuals – Athletes and those in high-risk professions can use Velmorastrin+ to proactively protect their brain.
Reduced symptoms post-injury – Helps alleviate symptoms like brain fog, headaches, dizziness, and fatigue.
Supports long-term brain health – Ingredients that promote neuroplasticity and overall cognitive well-being.
o Use simple, high-quality icons to visually represent each benefit.
3. Mechanism of Action Section:
o Explain how Velmorastrin+ works, focusing on the unique mechanisms of action without disclosing proprietary details. For example:
“Targets neuroinflammation, oxidative stress, and mitochondrial function to support brain recovery.”
Include infographics or simple diagrams showing how the supplement improves brain health by acting on multiple pathways.
4. Educational Section:
o This section, placed either below the hero section or above the FAQ section, will provide visitors with clear, digestible educational content about concussions. Topics may include:
What is a concussion?
Symptoms of concussions.
Long-term risks of untreated concussions.
The role of brain supplements in recovery.
Statistics and facts about concussions.
o This section is meant to establish Velmorastrin+ as a trusted authority on concussion care and brain health, driving credibility before visitors reach the CTA.
5. Educational Resources / Free Download:
o Offer a free eBook or concussion recovery guide as an incentive for visitors to provide their email. The guide should be high-quality and offer value (e.g., “The Silver Harbor Field Notebook”).
o Include a lead capture form (integrated with Mailchimp or a similar tool) that collects name and email addresses in exchange for the guide.
6. Blog Section:
o Create a blog section with regularly updated articles focusing on topics like:
Concussion prevention and recovery tips.
The science behind concussion supplements.
Brain health maintenance for athletes and high-risk populations.
Interviews with healthcare experts or athletes discussing concussions.
o The blog should drive SEO and increase organic traffic to the website while positioning Velmorastrin+ as an expert in brain health.
7. Social Proof and Testimonials:
o Add sample or hypothetical testimonials from athletes, military personnel, or healthcare professionals who would use a product like Velmorastrin+.
o Incorporate high-quality images (e.g., stock photos or graphics) alongside these testimonials to increase credibility.
8. FAQ Section:
o A simple FAQ section answering common questions about the product, such as:
What is Velmorastrin+?
How does it help with concussion recovery?
Who can benefit from it?
Are there any side effects?
o This section should reassure visitors by addressing safety and benefits.
9. Compliance & Disclaimers:
o Include all necessary disclaimers (e.g., “These statements have not been evaluated by the KTV”) and certifications (e.g., “Manufactured in a GMP-Certified Facility”).
5. Functional Requirements
1. Platform:
The website must be built on Wix for ease of use, so we can make future edits or updates without technical expertise. It should leverage Wix’s SEO features and be integrated with Google Analytics for tracking.
2. Lead Capture Integration:
The site must include a lead capture form integrated with Mailchimp or another email marketing platform to collect user data. Ensure all data is stored securely and complies with GDPR regulations.
3. Mobile Responsiveness:
The landing page must be fully responsive across all devices (desktop, tablet, and mobile), ensuring a seamless experience for users.
4. SEO Best Practices:
Implement basic SEO techniques (e.g., meta titles, descriptions, keywords) to ensure that the page is optimized for search engines. Use heading tags appropriately to highlight key sections.
5. Fast Load Times:
Optimize the site for fast load times. Compress images and streamline any large media files to ensure visitors do not bounce due to slow page performance.
6. Additional Features to Consider
1. Interactive Elements (Optional):
Consider adding a quiz (e.g., “Are You at Risk for a Concussion?”) or a poll to engage users and collect more data on their interest and concerns.
o Quizzes can help personalize the user experience while allowing you to gather insights about your audience.
2. Exit-Intent Popup offering visitors a free guide or other incentives could help capture users just before they leave the page, increasing conversions. This feature could prompt users who were about to exit to sign up for updates or download the eBook.
3. A/B Testing Capabilities:
If possible, include A/B testing functionality on key elements like CTAs and form placements, so we can optimize the site’s conversion rate based on performance data.
7. Deliverables
1. Fully functional, mobile-responsive Wix website that meets the design and functional requirements outlined above.
2. Integration of lead capture form with Mailchimp or other marketing platforms.
3. Google Analytics setup for tracking user behavior, conversions, and traffic.
4. Source files for any custom graphics or visuals used on the site.
5. A handover guide or documentation on how we can make simple updates to the site using Wix.
Athletes, Military Personnel and Veterans, Healthcare Professionals, Older adults
1 page

```html
<!DOCTYPE html>
<html lang="en">
<head>
<meta charset="utf-8">
<title>Velmorastrin+ | Guard Your Days</title>
<link href="https://fonts.googleapis.com/css2?family=Inter:wght@400;500;600;700;800&display=swap" rel="stylesheet">
<style>
:root{
  --teal:#19a4b3;
  --blue:#1b5d9b;
  --blue-deep:#164a82;
  --ink:#1d3f72;
  --text:#4a5566;
  --line:#d8dee6;
  --light:#f1f3f6;
  --white:#ffffff;
  --star:#f6b31b;
}
*{box-sizing:border-box;margin:0;padding:0}
html,body{width:1200px;height:4087px;overflow:hidden}
body{font-family:"Inter",sans-serif;color:var(--text);background:var(--white);position:relative}
.abs{position:absolute}
section,header,footer{position:absolute;left:0;width:1200px;overflow:hidden}
.eyebrow{font-size:15px;font-weight:700;letter-spacing:2.5px;color:var(--teal);text-transform:uppercase}
.eyebrow.sm{font-size:12px;letter-spacing:1.6px}
h1,h2,h3{color:var(--ink);font-weight:700}
.brand{font-weight:600;color:var(--blue);font-size:15px;display:flex;align-items:center;gap:8px}
.brand .dot{width:12px;height:12px;border-radius:50%;background:var(--teal)}

/* hero */
.hero{top:0;height:555px}
.hero-photo{position:absolute;inset:0;background:linear-gradient(180deg,#b9cfe0 0%,#d7e3ec 35%,#aebfcd 62%,#6d6558 100%)}
.hero-fade{position:absolute;inset:0;background:linear-gradient(90deg,rgba(255,255,255,.75) 0%,rgba(255,255,255,.35) 45%,rgba(255,255,255,0) 70%)}
.hero .brand{left:151px;top:34px}
.nav{left:446px;top:14px;display:flex;height:62px;align-items:center;font-size:10.5px;color:var(--ink);font-weight:500;white-space:nowrap}
.nav a{color:inherit;text-decoration:none;padding:0 9px;height:62px;display:flex;align-items:center}
.nav a.active{background:var(--teal);color:#fff;padding:0 12px;margin-right:4px}
.btn-contact{left:952px;top:38px;width:97px;height:37px;border-radius:20px;background:var(--blue-deep);color:#fff;font-size:11px;font-weight:600;display:flex;align-items:center;justify-content:center}
.hero .eyebrow{left:152px;top:187px;font-size:19px}
.hero h1{left:151px;top:216px;font-size:46px;line-height:47px;font-weight:800;color:var(--ink);letter-spacing:-1px}
.hero .lede{left:152px;top:321px;font-size:11.5px;line-height:16px;color:#233;width:460px}
.btn-guide{left:151px;top:371px;width:236px;height:35px;border-radius:20px;border:2px solid var(--blue-deep);background:#fff;display:flex;align-items:center;font-size:10.5px;font-weight:600;color:var(--blue-deep)}
.btn-guide .ic{width:40px;height:31px;border-radius:16px 0 0 16px;background:var(--blue-deep);display:flex;align-items:center;justify-content:center;margin-right:13px}
.slider-dots{left:155px;top:474px;display:flex;gap:8px;align-items:center}
.slider-dots .bar{width:48px;height:4px;background:#fff;border-radius:2px}
.slider-dots .ring{width:12px;height:12px;border-radius:50%;border:2px solid var(--teal)}
.arrow-btn{width:34px;height:34px;display:flex;align-items:center;justify-content:center}
.hero .prev{left:13px;top:273px;background:rgba(255,255,255,.35)}
.hero .next{left:1154px;top:273px;background:var(--blue)}

/* benefits */
.benefits{top:555px;height:489px;background:linear-gradient(90deg,#eaf3f7 0%,#f6fbfd 100%)}
.benefits .panel{position:absolute;left:0;top:0;width:508px;height:489px;background:linear-gradient(160deg,#1a5b9b 0%,#1a77a8 70%,#1d8fb5 100%)}
.benefits .eyebrow{left:151px;top:100px;font-size:19px;color:#5fd3dc}
.benefits h2{left:151px;top:133px;font-size:36px;line-height:40px;color:#fff;font-weight:600}
.benefits .intro{left:151px;top:264px;width:200px;font-size:10.5px;line-height:16px;color:#dbe8f3}
.benefits .ctrl{left:151px;top:365px;display:flex;gap:7px;align-items:flex-end}
.benefits .ctrl .arrow-btn{width:32px;height:32px;background:rgba(255,255,255,.15)}
.benefits .ctrl .more{font-size:9px;letter-spacing:1.5px;color:#fff;margin-left:10px;font-weight:600}
.b-card{position:absolute;top:91px;width:194px;height:309px;background:#f3f7fa;box-shadow:0 8px 24px rgba(20,60,100,.18);padding:29px 0 0 0}
.b-card .icon{margin-left:18px;width:70px;height:80px;border-radius:10px;background:linear-gradient(135deg,#e1f0f6,#cfe6ee)}
.b-card h3{margin-top:22px;border-left:3px solid var(--teal);padding:0 12px 0 15px;font-size:14.5px;line-height:19px;color:var(--blue-deep);font-weight:600}
.b-card p{padding:18px 18px 0 18px;font-size:10.5px;line-height:16px;color:#5a6474}
.b-card.faded{opacity:.45}

/* mechanism */
.mechanism{top:1044px;height:519px}
.mechanism .eyebrow{left:149px;top:102px}
.mechanism h2{left:149px;top:130px;width:420px;font-size:26.5px;line-height:32px;font-weight:600}
.mechanism h2 em{font-style:normal;color:var(--teal)}
.mechanism .point{left:149px;top:285px;width:410px;font-size:12px;line-height:18px;display:flex;gap:10px}
.phone-box{left:149px;top:338px;width:245px;height:70px;background:linear-gradient(90deg,#17497f,#1a88a8);display:flex;align-items:center;padding-left:15px;color:#fff}
.phone-box .ic{width:37px;height:37px;border-radius:8px;background:rgba(255,255,255,.2);display:flex;align-items:center;justify-content:center;margin-right:20px}
.phone-box small{display:block;font-size:10px;letter-spacing:.5px}
.phone-box strong{display:block;font-family:Georgia,serif;font-size:23px;font-weight:400;margin-top:2px}
.diagram{left:606px;top:54px;width:443px;height:386px;background:linear-gradient(135deg,#e6edf5 0%,#dbe4ef 55%,#d9d5ea 100%);box-shadow:0 10px 30px rgba(20,60,100,.12)}

/* educational resource */
.resource{top:1563px;height:475px;background:linear-gradient(90deg,#1a4f88 0%,#1a6ea7 60%,#1a8ab7 100%)}
.resource-photo{position:absolute;left:0;top:0;width:640px;height:475px;background:linear-gradient(90deg,#8d9aa8 0%,#a2a6a6 35%,#5b6e86 75%,rgba(26,95,155,0) 100%)}
.resource .eyebrow{left:598px;top:78px;color:#5fd3dc;font-size:12px;letter-spacing:1.6px}
.resource h2{left:598px;top:101px;width:400px;font-size:27px;line-height:30px;color:#fff;font-weight:500}
.resource .sub{left:598px;top:176px;width:400px;font-size:10px;line-height:15px;color:#e4eef6}
.resource form{position:absolute;left:598px;top:240px;width:391px}
.field{height:42px;border-bottom:1px solid rgba(255,255,255,.55);font-size:9.5px;font-weight:600;color:#fff;display:flex;align-items:center;padding-top:6px}
.btn-submit{margin-top:22px;width:97px;height:35px;border-radius:18px;background:#fff;color:var(--blue);font-size:11px;font-weight:600;display:flex;align-items:center;justify-content:center}

/* blog */
.blog{top:2038px;height:523px}
.post{position:absolute;top:92px;width:266px}
.post .thumb{height:151px;background:linear-gradient(135deg,#b8c7d6,#6e8aa6)}
.post .meta{margin-top:22px;font-size:10px;display:flex;gap:16px;color:#556}
.post .meta i{font-style:normal;color:var(--blue)}
.post h3{margin-top:14px;font-size:15.5px;line-height:20px;font-weight:500;color:var(--blue-deep)}
.post p{margin-top:11px;font-size:10px;line-height:16px}
.post .more{margin-top:16px;font-size:10px;font-weight:600;color:var(--teal)}
.blog h2{left:784px;top:134px;font-size:32px;font-weight:600}
.blog .intro{left:784px;top:184px;width:265px;font-size:10px;line-height:16px}
.btn-blogs{left:784px;top:317px;width:113px;height:34px;border-radius:18px;background:var(--blue-deep);color:#fff;font-size:10px;font-weight:600;display:flex;align-items:center;justify-content:center}

/* testimonials */
.testimonials{top:2561px;height:499px;background:#eff1f4}
.testi-photo{position:absolute;left:0;top:0;width:567px;height:499px;background:linear-gradient(135deg,#3f7fb8,#5a9cc8 55%,#7fb6d6)}
.testimonials .eyebrow{left:600px;width:415px;top:100px;text-align:center;font-size:12px;letter-spacing:1.6px}
.testimonials h2{left:600px;width:415px;top:117px;text-align:center;font-size:27px;line-height:30px;font-weight:500}
.testi-strip{left:657px;top:197px;width:441px;height:194px;background:#fff}
.t-card{position:absolute;width:310px}
.t-card.first{left:440px;top:243px;height:148px;background:#fff;border-radius:8px;box-shadow:0 6px 20px rgba(0,0,0,.08);padding:28px 0 0 40px;width:340px}
.t-card.second{left:815px;top:243px;padding-top:28px}
.stars{color:var(--star);font-size:12px;letter-spacing:1px}
.t-card .name{font-family:Georgia,serif;color:var(--teal);font-size:11px;margin-top:4px}
.t-card .role{font-size:10px;margin-top:4px}
.t-card p{font-size:9.5px;line-height:14px;margin-top:12px;width:275px}
.avatar{position:absolute;width:86px;height:86px;border-radius:50%;background:#c8d4df;border:3px solid #fff}
.t-dots{left:777px;top:2988px;display:flex;gap:9px;align-items:center}
.t-dots span{width:7px;height:7px;border-radius:50%;background:#c9ced6}
.t-dots span.on{width:14px;height:6px;border-radius:3px;background:var(--teal)}

/* learn */
.learn{top:3060px;height:389px}
.learn .intro{left:0;width:1200px;top:88px;text-align:center;font-size:16.5px;line-height:23px;color:var(--ink)}
.learn .intro b{color:var(--teal)}
.topic{position:absolute;top:160px;width:180px;text-align:center}
.topic .icon{width:70px;height:70px;margin:0 auto;border-radius:50%;background:linear-gradient(135deg,#d7f0ee,#e3eefb)}
.topic h3{margin-top:22px;font-size:13.5px;line-height:18px;font-weight:600;color:var(--ink)}
.vrule{position:absolute;top:170px;width:1px;height:119px;background:var(--line)}

/* faq */
.faq{top:3449px;height:452px;background:var(--light)}
.faq .eyebrow{left:149px;top:84px;font-size:12px;letter-spacing:1.6px}
.faq h2{left:149px;top:109px;font-size:30px;line-height:36px;font-weight:600}
.faq .intro{left:149px;top:193px;width:360px;font-size:10.5px;line-height:16px}
.contact-row{position:absolute;left:149px;display:flex;gap:15px;align-items:center}
.contact-row .ic{width:36px;height:36px;border-radius:6px;background:#78c6c9;display:flex;align-items:center;justify-content:center}
.contact-row strong{display:block;font-size:12.5px;font-weight:600;color:var(--ink)}
.contact-row span{display:block;font-size:10px;margin-top:2px}
.qa{position:absolute;left:600px;width:420px}
.qa .q{display:flex;justify-content:space-between;font-size:12px;font-weight:600;color:var(--ink)}
.qa .q.open{color:var(--teal)}
.qa .q i{font-style:normal;font-weight:400;color:#556;font-size:17px;line-height:12px}
.qa .a{margin-top:12px;font-size:10px;line-height:16px;width:385px}

/* footer */
.site-footer{top:3901px;height:186px;background:linear-gradient(90deg,#1a3f70,#173a6b)}
.site-footer .brand{left:151px;top:84px;color:#fff;font-size:16px}
.site-footer .sep{position:absolute;left:320px;top:60px;width:1px;height:80px;background:rgba(255,255,255,.3)}
.foot-nav{left:355px;top:65px;display:flex;gap:22px;font-size:10.5px;color:#fff}
.copy{left:355px;top:89px;font-size:10.5px;color:#b8c6d8}
.copy b{color:#fff;font-weight:500}
.socials{left:355px;top:117px;display:flex;gap:9px}
.socials span{width:13px;height:13px;border-radius:50%;background:#fff}
</style>
</head>
<body>

<header class="hero">
  <div class="hero-photo" role="img" aria-label="Woman meditating on a wooden pier beside a misty mountain lake"></div>
  <div class="hero-fade"></div>
  <div class="abs brand"><span class="dot"></span>Velmorastrin+</div>
  <nav class="abs nav">
    <a class="active">Home</a><a>Benefit</a><a>Mechanism of Action</a><a>Education</a><a>Blog</a><a>Testimonial</a><a>FAQ</a>
  </nav>
  <div class="abs btn-contact">Contact Us</div>
  <div class="abs eyebrow">Guard Your Days.</div>
  <h1 class="abs">Bounce Back with<br>Velmorastrin+</h1>
  <p class="abs lede">Briefly describe the supplement’s primary benefits, e.g., “Advanced nutraceutical formulation supporting brain health and faster concussion recovery.”</p>
  <div class="abs btn-guide"><span class="ic"><svg width="16" height="14" viewBox="0 0 16 14" fill="none" stroke="#fff" stroke-width="1.4"><path d="M1 2h5a2 2 0 0 1 2 2v9a2 2 0 0 0-2-2H1zM15 2h-5a2 2 0 0 0-2 2v9a2 2 0 0 1 2-2h5z"/></svg></span>Download Free Recovery Guide</div>
  <div class="abs slider-dots"><span class="bar"></span><span class="ring"></span><span class="ring"></span></div>
  <div class="abs arrow-btn prev"><svg width="10" height="14" viewBox="0 0 10 14" fill="none" stroke="#fff" stroke-width="1.5"><path d="M8 1 2 7l6 6"/></svg></div>
  <div class="abs arrow-btn next"><svg width="10" height="14" viewBox="0 0 10 14" fill="none" stroke="#fff" stroke-width="1.5"><path d="m2 1 6 6-6 6"/></svg></div>
</header>

<section class="benefits">
  <div class="panel"></div>
  <div class="abs eyebrow">Benifits</div>
  <h2 class="abs">We Provide<br>The Best<br>Befenits.</h2>
  <p class="abs intro">Velmorastrin+ seeks to fill this gap by providing a science-backed, multi-ingredient formulation designed to helping the brain recover faster and more effectively.</p>
  <div class="abs ctrl">
    <span class="arrow-btn"><svg width="9" height="14" viewBox="0 0 10 14" fill="none" stroke="#fff" stroke-width="1.5"><path d="M8 1 2 7l6 6"/></svg></span>
    <span class="arrow-btn"><svg width="9" height="14" viewBox="0 0 10 14" fill="none" stroke="#fff" stroke-width="1.5"><path d="m2 1 6 6-6 6"/></svg></span>
    <span class="more">MORE</span>
  </div>
  <article class="b-card" style="left:406px"><div class="icon" role="img" aria-label="Shield and brain line icon"></div><h3>Faster recovery from concussions</h3><p>Velmorastrin+ accelerates recovery by reducing neuroinflammation and oxidative stress.</p></article>
  <article class="b-card" style="left:619px"><div class="icon" role="img" aria-label="Brain line icon"></div><h3>Protection against long-term brain damage</h3><p>The supplement helps prevent lasting cognitive impairment from multiple or severe concussions.</p></article>
  <article class="b-card" style="left:833px"><div class="icon" role="img" aria-label="Mitochondrion line icon"></div><h3>Scientifically backed multi-pathway neuroprotection</h3><p>Targets inflammation, oxidative damage, mitochondrial function, and synaptic health.</p></article>
  <article class="b-card faded" style="left:1046px"><div class="icon" role="img" aria-label="Head profile line icon"></div><h3>Improved cognitive function</h3><p>Enhances mental clarity, focus, and energy post-concussion.</p></article>
</section>

<section class="mechanism">
  <div class="abs eyebrow sm">Mechanism of Action</div>
  <h2 class="abs">Experience the Velmorastrin+ works, focusing on the <em>unique mechanisms of action</em> without disclosing proprietary.</h2>
  <p class="abs point"><svg width="14" height="16" viewBox="0 0 14 16" fill="none" stroke="#19a4b3" stroke-width="1.4"><path d="M7 1 1.5 3v4.5C1.5 11 4 13.6 7 15c3-1.4 5.5-4 5.5-7.5V3z"/><path d="m4.5 8 2 2 3-3.5"/></svg><span>Targets neuroinflammation, oxidative stress, and mitochondrial function to support brain recovery.</span></p>
  <div class="abs phone-box"><span class="ic"><svg width="18" height="18" viewBox="0 0 24 24" fill="#fff"><path d="M6.6 10.8a15.1 15.1 0 0 0 6.6 6.6l2.2-2.2a1 1 0 0 1 1-.25 11.4 11.4 0 0 0 3.6.57 1 1 0 0 1 1 1V20a1 1 0 0 1-1 1A17 17 0 0 1 3 4a1 1 0 0 1 1-1h3.5a1 1 0 0 1 1 1c0 1.25.2 2.45.57 3.57a1 1 0 0 1-.25 1z"/></svg></span><div><small>FREE CONSULTATION</small><strong>555.014.2290</strong></div></div>
  <div class="abs diagram" role="img" aria-label="Infographic: a central brain linked to four brain chemicals — serotonin, the mood stabilizer; dopamine, the reward chemical; oxytocin, the love hormone; and endorphine, the natural pain reliever"></div>
</section>

<section class="resource">
  <div class="resource-photo" role="img" aria-label="Man reading a tablet on a sofa beside a grey cat"></div>
  <div class="abs eyebrow">Educational Resources</div>
  <h2 class="abs">The Silver Harbor Field Notebook</h2>
  <p class="abs sub">Offer a <b>Free eBook or concussion recovery guide</b> as an incentive for visitors to provide their email. The guide should be high-quality and offer value.</p>
  <form>
    <div class="field">NAME</div>
    <div class="field">EMAIL</div>
    <div class="field">PHONE NUMBER</div>
    <div class="btn-submit">Submit</div>
  </form>
</section>

<section class="blog">
  <article class="post" style="left:151px"><div class="thumb" role="img" aria-label="Doctor reviewing brain scans with a patient"></div><div class="meta"><span><i>▭</i> Octoer 29th, 2024</span><span><i>▢</i> 0</span></div><h3>Provide high-level, non-proprietary information about concussions, brain health.</h3><p>Velmorastrin+ seeks to fill this gap by providing a science-backed, multi-ingredient formulation designed to reduce neuroinflammation...</p><div class="more">Read More →</div></article>
  <article class="post" style="left:456px"><div class="thumb" style="background:linear-gradient(180deg,#c5d6e2,#8fb0c6 55%,#5f87a4)" role="img" aria-label="Person standing on a brain-shaped island in the sea"></div><div class="meta"><span><i>▭</i> Octoer 29th, 2024</span><span><i>▢</i> 0</span></div><h3>Provide high-level, non-proprietary information about concussions, brain health.</h3><p>Velmorastrin+ seeks to fill this gap by providing a science-backed, multi-ingredient formulation designed to reduce neuroinflammation...</p><div class="more">Read More →</div></article>
  <h2 class="abs">Blogs &amp; Articles</h2>
  <p class="abs intro">Velmorastrin+ seeks to fill this gap by providing a science-backed, multi-ingredient formulation designed to reduce neuroinflammation, oxidative stress, and support mitochondrial function, helping the brain recover faster and more effectively. Our goal is to raise awareness of this innovative approach to concussion care.</p>
  <div class="abs btn-blogs">View All Blogs</div>
</section>

<section class="testimonials">
  <div class="testi-photo" role="img" aria-label="Smiling older couple shaking hands with a caregiver"></div>
  <div class="abs eyebrow">Testimonials</div>
  <h2 class="abs">What Our Clients Say<br>About Us</h2>
  <div class="abs testi-strip"></div>
  <div class="t-card first"><div class="stars">★★★★★</div><div class="name">Mira Solden</div><div class="role">Artisan</div><p>Lorem ipsum dolor sit amet consectetur. Lorem accumsan sit quis lacus varius. Lectus quis mauris amet dictum suspendisse aenean nullam. Mauris senectus.</p></div>
  <div class="avatar" role="img" aria-label="Client portrait" style="left:664px;top:226px"></div>
  <div class="t-card second"><div class="stars">★★★★★</div><div class="name">Teo Varga</div><div class="role">Artisan</div><p>Lorem ipsum dolor sit amet consectetur. Lorem accumsan sit quis lacus varius. Lectus quis mauris amet dictum suspendisse aenean nullam. Mauris senectus.</p></div>
  <div class="avatar" role="img" aria-label="Client portrait" style="left:999px;top:224px"></div>
</section>
<div class="abs t-dots"><span></span><span class="on"></span><span></span><span></span></div>

<section class="learn">
  <p class="abs intro">Establish <b>Velmorastrin+</b> as a trusted authority on concussion care and<br>brain health, driving credibility before visitors reach the CTA.</p>
  <div class="topic" style="left:113px"><div class="icon" role="img" aria-label="Head with medical cross icon"></div><h3>What is a<br>concussion?</h3></div>
  <div class="vrule" style="left:282px"></div>
  <div class="topic" style="left:275px"><div class="icon" role="img" aria-label="Head with brain icon"></div><h3>Symptoms of<br>concussions.</h3></div>
  <div class="vrule" style="left:452px"></div>
  <div class="topic" style="left:477px"><div class="icon" role="img" aria-label="Warning sign with brain icon"></div><h3>Long-term risks of<br>untreated concussions.</h3></div>
  <div class="vrule" style="left:679px"></div>
  <div class="topic" style="left:689px"><div class="icon" role="img" aria-label="Brain circuit icon"></div><h3>The role of brain<br>supplements in<br>recovery.</h3></div>
  <div class="vrule" style="left:878px"></div>
  <div class="topic" style="left:889px"><div class="icon" role="img" aria-label="Bar chart icon"></div><h3>Statistics and acts<br>about concussions.</h3></div>
</section>

<section class="faq">
  <div class="abs eyebrow">FAQ</div>
  <h2 class="abs">Frequently Asking<br>Question</h2>
  <p class="abs intro">Velmorastrin+ seeks to fill this gap by providing a science-backed, multi-ingredient formulation designed to reduce neuroinflammation, oxidative stress, and support mitochondrial function.</p>
  <div class="contact-row" style="top:277px"><span class="ic"><svg width="16" height="12" viewBox="0 0 16 12" fill="none" stroke="#fff" stroke-width="1.4"><rect x="1" y="1" width="14" height="10" rx="1"/><path d="m1 2 7 5 7-5"/></svg></span><div><strong>Mail Address</strong><span>hello@velmorastrin-mail.com</span></div></div>
  <div class="contact-row" style="top:328px"><span class="ic"><svg width="15" height="15" viewBox="0 0 24 24" fill="#fff"><path d="M6.6 10.8a15.1 15.1 0 0 0 6.6 6.6l2.2-2.2a1 1 0 0 1 1-.25 11.4 11.4 0 0 0 3.6.57 1 1 0 0 1 1 1V20a1 1 0 0 1-1 1A17 17 0 0 1 3 4a1 1 0 0 1 1-1h3.5a1 1 0 0 1 1 1c0 1.25.2 2.45.57 3.57a1 1 0 0 1-.25 1z"/></svg></span><div><strong>Phone Number</strong><span>555-014-2290</span></div></div>
  <div class="qa" style="top:110px"><div class="q open">What is Velmorastrin+?<i>–</i></div><p class="a">Velmorastrin+ seeks to fill this gap by providing a science-backed, multi-ingredient formulation designed to reduce neuroinflammation, oxidative stress, and support mitochondrial function, helping the brain recover faster and more effectively. Velmorastrin+ seeks to fill this gap by providing a science-backed, multi-ingredient formulation designed to reduce neuroinflammation, oxidative stress, and support mitochondrial function, helping the brain recover faster and more effectively.</p></div>
  <div class="qa" style="top:287px"><div class="q">How does it help with concussion recovery?<i>+</i></div></div>
  <div class="qa" style="top:322px"><div class="q">Who can benefit from it?<i>+</i></div></div>
  <div class="qa" style="top:356px"><div class="q">Are there any side effects?<i>+</i></div></div>
</section>

<footer class="site-footer">
  <div class="abs brand"><span class="dot"></span>Velmorastrin+</div>
  <div class="sep"></div>
  <nav class="abs foot-nav"><span>Home</span><span>Benefit</span><span>Mechanism of Action</span><span>Education</span><span>Blog</span><span>Testimonial</span><span>FAQ</span><span>Contact Us</span></nav>
  <p class="abs copy">Copyright © 2024 <b>velmorastrin.com</b>. All Rights Reserved.</p>
  <div class="abs socials"><span></span><span></span><span></span><span></span></div>
</footer>

</body>
</html>
```